Marlow Label design search/01

We need a label design for a new customers chemical products. The label is 275mm wide and 165mm high. The design will be simple with lots of space left for us to thermally print the information required on each label. This thermal print is black. From the top down 70mm the label will be white. The logo size will be about 50mm-55mm across and 40mm-45mm down. The logo position needs to be 1 of the following positions
a) Cetred at the bottom
b) Centred at the top
c) At the bottom no closer than 70mm to the right edge
The attached logo has 8 logos on it and we would like the Marlow Reagents on the left.
Requirements
Must have
- Logo
- look at attached info
Nice to have
- Simple and clean

```html
<!DOCTYPE html>
<html lang="en">
<head>
<meta charset="utf-8">
<title>Marlow Reagents – Label Concepts</title>
<link href="https://fonts.googleapis.com/css2?family=Open+Sans:wght@700&display=swap" rel="stylesheet">
<style>
  :root {
    --brand-red: #a81e25;
    --label-white: #ffffff;
    --page-bg: #ecebe8;
    --water-deep: #5a9ad8;
    --water-mid: #9fcbef;
    --water-light: #eef6fc;
  }
  * { margin: 0; padding: 0; box-sizing: border-box; }
  html, body {
    width: 918px;
    height: 1200px;
    overflow: hidden;
    background: var(--page-bg);
  }
  .sheet {
    position: relative;
    width: 918px;
    height: 1200px;
  }
  .label {
    position: absolute;
    left: 64px;
    width: 790px;
    height: 475px;
    background: var(--label-white);
    overflow: hidden;
    box-shadow: 0 2px 8px rgba(0,0,0,0.18);
  }
  .label--red { top: 62px; }
  .label--water { top: 600px; }

  .brand {
    position: absolute;
    top: 64px;
    left: 0;
    width: 100%;
    text-align: center;
    font-family: "Open Sans", sans-serif;
    font-weight: 700;
    color: var(--brand-red);
    font-size: 30px;
    letter-spacing: 1px;
    line-height: 36px;
  }

  .print-band {
    position: absolute;
    left: 0;
    top: 202px;
    width: 100%;
    height: 273px;
    background: var(--brand-red);
  }
  .print-band__tab {
    position: absolute;
    left: 215px;
    bottom: 0;
    width: 360px;
    height: 15px;
    background: var(--label-white);
    border-radius: 4px 4px 0 0;
  }

  .water-art {
    position: absolute;
    left: 0;
    top: 196px;
    width: 100%;
    height: 279px;
    background: linear-gradient(180deg, var(--water-deep) 0%, var(--water-mid) 25%, var(--water-light) 70%, var(--water-mid) 100%);
  }
</style>
</head>
<body>
  <main class="sheet">
    <section class="label label--red">
      <div class="brand">Marlow Reagents</div>
      <div class="print-band">
        <div class="print-band__tab"></div>
      </div>
    </section>

    <section class="label label--water">
      <div class="brand">Marlow Reagents</div>
      <div class="water-art" role="img" aria-label="Watercolour illustration of blue water with a wavy surface and rising bubbles"></div>
    </section>
  </main>
</body>
</html>
```